Business Card Revision

Need to redesign my business cards for a new professional look. We are a courier company. You can go to www.qvrunners.com to see what we do. The trucks have an old company name (Sprout) on them but that is the company we are just now
changing the name.

Target Market(s)

Potential clients. We service the automotive, plumbing, printing, air freight industries as well as many others.

Industry/Entity Type

Business

Contact Information for Business Card

QVmotion
20864 Lark Fenmore Parkway
Cincinnati, Oh 45873

Thomas R. Wendall
President

tom@qvrunners.com

Main: (513) 555-0147

```html
<!DOCTYPE html>
<html lang="en">
<head>
<meta charset="utf-8">
<title>QV Runners – Business Card</title>
<link href="https://fonts.googleapis.com/css2?family=Source+Sans+3:wght@400;600;700&display=swap" rel="stylesheet">
<style>
  :root {
    --page-bg: #e9e7e3;
    --card-bg: #ffffff;
    --brand-blue: #1f78c8;
    --brand-green: #35b34a;
    --ink: #1b1b1b;
    --band-black: #141414;
    --band-black-light: #2a2a2a;
    --address-ink: #f4f4f4;
  }
  * { box-sizing: border-box; margin: 0; padding: 0; }
  html, body {
    width: 1200px; height: 892px; overflow: hidden;
    background: var(--page-bg);
    font-family: "Source Sans 3", Arial, sans-serif;
  }
  .canvas { position: relative; width: 1200px; height: 892px; }
  .business-card {
    position: absolute; left: 75px; top: 146px;
    width: 1050px; height: 600px;
    background: var(--card-bg);
    border-radius: 30px;
    overflow: hidden;
    box-shadow: 0 8px 24px rgba(0,0,0,0.18);
  }
  .brand {
    position: absolute; left: 90px; top: 70px;
    display: flex; align-items: center; gap: 22px;
  }
  .brand-mark { width: 70px; height: 70px; background: var(--brand-blue); }
  .brand-name {
    font-weight: 700; font-size: 86px; line-height: 1;
    letter-spacing: 2px; color: var(--brand-green);
    text-transform: uppercase;
  }
  .person { position: absolute; left: 100px; top: 255px; }
  .person-name {
    font-weight: 700; font-size: 50px; color: var(--brand-green); line-height: 1.05;
  }
  .person-title {
    font-weight: 400; font-size: 36px; color: var(--ink); margin-top: 6px;
  }
  .divider {
    position: absolute; left: 560px; top: 240px;
    width: 3px; height: 118px; background: var(--ink);
  }
  .contact-list { position: absolute; left: 595px; top: 236px; list-style: none; }
  .contact-item {
    display: flex; align-items: center; gap: 16px;
    font-size: 31px; color: var(--ink); line-height: 1; margin-bottom: 11px;
  }
  .contact-icon { width: 24px; height: 24px; flex: none; }
  .card-bands { position: absolute; left: 0; top: 0; width: 1050px; height: 600px; }
  .address {
    position: absolute; left: 0; right: 0; top: 522px;
    text-align: center; font-size: 32px; color: var(--address-ink);
    letter-spacing: 0.3px;
  }
</style>
</head>
<body>
<main class="canvas">
  <section class="business-card">
    <svg class="card-bands" viewBox="0 0 1050 600" aria-hidden="true">
      <defs>
        <linearGradient id="blackBand" x1="0" y1="0" x2="0" y2="1">
          <stop offset="0" stop-color="var(--band-black-light)"/>
          <stop offset="1" stop-color="var(--band-black)"/>
        </linearGradient>
      </defs>
      <path d="M0 422 Q 620 436 1050 388 L1050 600 L0 600 Z" fill="var(--brand-blue)"/>
      <path d="M0 434 Q 620 448 1050 400 L1050 600 L0 600 Z" fill="var(--brand-green)"/>
      <path d="M0 456 Q 620 470 1050 422 L1050 600 L0 600 Z" fill="url(#blackBand)"/>
    </svg>

    <div class="brand">
      <span class="brand-mark"></span>
      <span class="brand-name">QV Runners</span>
    </div>

    <div class="person">
      <p class="person-name">Thomas R. Wendall</p>
      <p class="person-title">President</p>
    </div>

    <span class="divider"></span>

    <ul class="contact-list">
      <li class="contact-item">
        <svg class="contact-icon" viewBox="0 0 24 24" aria-hidden="true">
          <rect width="24" height="24" rx="3" fill="var(--brand-blue)"/>
          <path d="M8 5c1 0 1.5 2.5 1.5 3s-1.5 1-1.5 1.5 2 4.5 4.5 4.5c.5 0 1-1.5 1.5-1.5s3 .5 3 1.5-1 3-3 3C9 17 5 12 5 8c0-2 2-3 3-3z" fill="#fff"/>
        </svg>
        <span>(513) 555-0147</span>
      </li>
      <li class="contact-item">
        <svg class="contact-icon" viewBox="0 0 24 24" aria-hidden="true">
          <rect width="24" height="24" rx="3" fill="var(--brand-blue)"/>
          <circle cx="12" cy="12" r="7" fill="none" stroke="#fff" stroke-width="1.8"/>
          <ellipse cx="12" cy="12" rx="3" ry="7" fill="none" stroke="#fff" stroke-width="1.4"/>
          <line x1="5" y1="12" x2="19" y2="12" stroke="#fff" stroke-width="1.4"/>
        </svg>
        <span>www.qvrunners.com</span>
      </li>
      <li class="contact-item">
        <svg class="contact-icon" viewBox="0 0 24 24" aria-hidden="true">
          <rect width="24" height="24" rx="3" fill="var(--brand-blue)"/>
          <rect x="5" y="7" width="14" height="10" fill="#fff"/>
          <path d="M5 7 L12 13 L19 7" fill="none" stroke="var(--brand-blue)" stroke-width="1.5"/>
        </svg>
        <span>tom@qvrunners.com</span>
      </li>
    </ul>

    <p class="address">20864 Lark Fenmore Parkway Cincinnati, Oh 45873</p>
  </section>
</main>
</body>
</html>
```